Business Card Design Project

We would like to have a new design for our Business Cards.
Please see attached JPEG to see the current.
We would like to be sober and clean, very professional.

Target Market(s)

IT Market

Industry/Entity Type

Business

Font styles to use
Serif
Sans Serif

Colors
ec1f27
f78f20
333333
5c5c5c
9d9d9d
e9e9e9
ffffff

Requirements
Must have
• It needs to be completely different than the current design (see attached),

```html
<!DOCTYPE html>
<html lang="en">
<head>
<meta charset="utf-8">
<title>NexaGrid Business Card</title>
<link href="https://fonts.googleapis.com/css2?family=Open+Sans:wght@400;600;700&display=swap" rel="stylesheet">
<style>
  :root {
    --page: #e9e9e9;
    --card: #1d1d1d;
    --card-edge: #333333;
    --emboss: #2c2c2c;
    --emboss-text: #3a3a3a;
    --accent: #ec1f27;
    --ink: #ffffff;
    --muted: #9d9d9d;
  }
  * { margin: 0; padding: 0; box-sizing: border-box; }
  html, body { width: 1200px; height: 816px; overflow: hidden; }
  body {
    background: var(--page);
    font-family: "Open Sans", Arial, sans-serif;
    position: relative;
  }
  .card {
    position: absolute;
    top: 254px;
    width: 540px;
    height: 308px;
    background: var(--card);
    border-radius: 4px;
    box-shadow: 0 6px 18px rgba(0,0,0,0.25);
    overflow: hidden;
  }
  .card-back { left: 30px; }
  .card-front { left: 630px; }

  .back-brand {
    position: absolute;
    left: 0; right: 0; top: 0; bottom: 0;
    display: flex;
    align-items: center;
    justify-content: center;
    gap: 18px;
  }
  .back-brand .mark {
    width: 62px; height: 62px;
    border-radius: 50%;
    background: var(--emboss);
  }
  .back-brand .name {
    font-weight: 700;
    font-size: 56px;
    letter-spacing: -1px;
    color: var(--emboss-text);
  }

  .front-brand {
    position: absolute;
    left: 30px;
    top: 104px;
    display: flex;
    align-items: center;
    gap: 12px;
  }
  .front-brand .mark {
    width: 40px; height: 40px;
    border-radius: 50%;
    background: var(--accent);
  }
  .front-brand .name {
    font-weight: 700;
    font-size: 34px;
    letter-spacing: -0.5px;
    color: var(--ink);
  }

  .divider {
    position: absolute;
    left: 268px;
    top: 118px;
    width: 1px;
    height: 150px;
    background: linear-gradient(var(--accent), rgba(236,31,39,0));
  }

  .contact {
    position: absolute;
    left: 282px;
    top: 38px;
    color: var(--ink);
  }
  .contact .person {
    color: var(--accent);
    font-weight: 700;
    font-size: 22px;
    line-height: 1.1;
  }
  .contact .role {
    font-size: 13px;
    margin-bottom: 10px;
  }
  .contact .address {
    font-size: 13px;
    line-height: 1.35;
    margin-bottom: 6px;
  }
  .contact ul { list-style: none; }
  .contact li {
    display: flex;
    align-items: center;
    gap: 8px;
    font-size: 13px;
    line-height: 19px;
  }
  .contact li svg { width: 11px; height: 11px; flex: none; fill: var(--accent); }
</style>
</head>
<body>

<div class="card card-back">
  <div class="back-brand">
    <span class="mark"></span>
    <span class="name">NexaGrid</span>
  </div>
</div>

<div class="card card-front">
  <div class="front-brand">
    <span class="mark"></span>
    <span class="name">NexaGrid</span>
  </div>

  <div class="divider"></div>

  <div class="contact">
    <p class="person">Daniel R. Hart</p>
    <p class="role">Managing Member</p>
    <p class="address">2250 Harbor Lane,<br>Fresno, CA 93721</p>
    <ul>
      <li>
        <svg viewBox="0 0 12 12" aria-hidden="true"><path d="M2.5 0.5l2 2.2-1 1.3c.7 1.5 1.8 2.7 3.4 3.5l1.3-1 2.3 2-1.3 2C5 10.2 1.5 6.6.5 2z"/></svg>
        <span>(555) 201-4410</span>
      </li>
      <li>
        <svg viewBox="0 0 12 12" aria-hidden="true"><rect x="2" y="0.5" width="8" height="3.5"/><rect x="0.5" y="4.5" width="11" height="5" rx="1"/><rect x="2.5" y="8" width="7" height="3.5"/></svg>
        <span>(555) 201-4411</span>
      </li>
      <li>
        <svg viewBox="0 0 12 12" aria-hidden="true"><path d="M3 0.5h6a1 1 0 0 1 1 1v9a1 1 0 0 1-1 1H3a1 1 0 0 1-1-1v-9a1 1 0 0 1 1-1zM3.2 1.8v7.4h5.6V1.8z"/></svg>
        <span>(555) 318-2290</span>
      </li>
      <li>
        <svg viewBox="0 0 12 12" aria-hidden="true"><path d="M0.5 2h11v8h-11zM1.5 3l4.5 3.5L10.5 3z" fill-rule="evenodd"/></svg>
        <span>daniel@lindenrowtech.com</span>
      </li>
      <li>
        <svg viewBox="0 0 12 12" aria-hidden="true"><path d="M6 .5a5.5 5.5 0 1 0 0 11 5.5 5.5 0 0 0 0-11zm0 1.2c.6.7 1.1 1.8 1.3 3.3H4.7C4.9 3.5 5.4 2.4 6 1.7zM4.7 6.3h2.6C7.1 7.8 6.6 8.9 6 9.6c-.6-.7-1.1-1.8-1.3-3.3zM1.8 5h1.6c.1-1.2.4-2.2.8-2.9A4.3 4.3 0 0 0 1.8 5zm0 1.3a4.3 4.3 0 0 0 2.4 3.1c-.4-.8-.7-1.8-.8-3.1zm6.8 0c-.1 1.3-.4 2.3-.8 3.1a4.3 4.3 0 0 0 2.4-3.1zm0-1.3h1.6a4.3 4.3 0 0 0-2.4-2.9c.4.7.7 1.7.8 2.9z"/></svg>
        <span>www.lindenrowtech.com</span>
      </li>
    </ul>
  </div>
</div>

</body>
</html>
```